Stationary Design - KM Facial Plastics

We are looking for a stylish and professional stationary design for a facial plastic surgeon. The stationary design will be for letterhead, business card, appointment cards and envelopes.
The design must be slick and aesthetically pleasing whilst incorporating the style of our logo as attached below.

Target Market(s)

Adults of all ages

Font styles to use
Serif
Script

Requirements
Must have
• Must be an aesthetically pleasing, stylish and professional design that includes the required information in a captivating layout.
• Must also be welcoming with a balanced design and a clean crisp finish.
• Details should include:
• Mr Tobias Wrenfield - Consultant Otolaryngologist & Facial Plastic Surgeon
• Phone: 03 5618 2947
• Fax: 03 5619 7084
• Email: info@kmfacialplastics.example.com.au
• Consulting from: Bendigo, Echuca, Epping, Waverley & Melbourne CBD
• Appointment Card should include:
• Date, time, fee and location as per the attached example.
• location addresses are:
• 31 Harlow Street Echuca Vic 3564
• 148 Brennock Street Ashvale Vic 3550
• Level 2, 217 Mabley Street, Epping Vic 3076
• Level 4, 263 Denholm Street Melbourne Vic 3000
Should not have
• Clutter

```html
<!DOCTYPE html>
<html lang="en">
<head>
<meta charset="utf-8">
<title>KM Facial Plastics – Business Card</title>
<link rel="stylesheet" href="https://fonts.googleapis.com/css2?family=Oswald:wght@500&family=Montserrat:wght@300;400&family=Playfair+Display:ital@1&family=Libre+Baskerville:wght@700&family=Cormorant+Garamond:wght@500&display=swap">
<style>
  :root {
    --backdrop: #e4e4e4;
    --card: #4a4a4a;
    --ink: #ffffff;
    --ink-soft: #d8d8d8;
    --silver: #c9c9c9;
    --rule: #bdbdbd;
  }
  * { box-sizing: border-box; margin: 0; padding: 0; }
  html, body { width: 1200px; height: 800px; overflow: hidden; }
  body {
    background: var(--backdrop);
    display: flex;
    align-items: center;
    justify-content: center;
    gap: 40px;
  }
  .card {
    width: 540px;
    height: 308px;
    background: var(--card);
    border-radius: 22px;
    position: relative;
    color: var(--ink);
  }

  /* Front */
  .card-front {
    display: flex;
    align-items: center;
    justify-content: center;
    padding: 0 18px;
  }
  .identity {
    text-align: right;
    padding-right: 14px;
    white-space: nowrap;
  }
  .identity-name {
    font-family: "Oswald", sans-serif;
    font-weight: 500;
    font-size: 24px;
    letter-spacing: 0.3px;
    line-height: 1.1;
    text-transform: uppercase;
  }
  .identity-role {
    font-family: "Montserrat", sans-serif;
    font-weight: 300;
    font-size: 8.5px;
    letter-spacing: 0.3px;
    line-height: 1.5;
    text-transform: uppercase;
    color: var(--ink-soft);
    margin-top: 4px;
  }
  .divider {
    width: 1px;
    height: 100px;
    background: var(--rule);
    flex: none;
  }
  .contact {
    padding-left: 14px;
    list-style: none;
    white-space: nowrap;
  }
  .contact-address {
    font-family: "Playfair Display", serif;
    font-style: italic;
    font-size: 12px;
    margin-bottom: 5px;
  }
  .contact-item {
    display: flex;
    align-items: center;
    gap: 6px;
    font-family: "Libre Baskerville", serif;
    font-weight: 700;
    font-size: 8.5px;
    line-height: 1.8;
  }
  .contact-item svg { width: 9px; height: 9px; flex: none; }

  /* Back */
  .card-back {
    display: flex;
    flex-direction: column;
    align-items: center;
  }
  .brand-name {
    margin-top: 96px;
    font-family: "Cormorant Garamond", serif;
    font-weight: 500;
    font-size: 30px;
    letter-spacing: 2px;
    color: var(--silver);
  }
  .locations {
    position: absolute;
    bottom: 46px;
    left: 0;
    right: 0;
    text-align: center;
    font-family: "Montserrat", sans-serif;
    font-weight: 400;
    font-size: 12.5px;
    letter-spacing: 0.3px;
  }
</style>
</head>
<body>
  <section class="card card-front" aria-label="Business card front">
    <div class="identity">
      <h1 class="identity-name">Mr Tobias Wrenfield</h1>
      <p class="identity-role">Consultant Otolaryngologist &amp;<br>Facial Plastic Surgeon</p>
    </div>
    <div class="divider"></div>
    <ul class="contact">
      <li class="contact-address">148 Brennock Street Ashvale</li>
      <li class="contact-item">
        <svg viewBox="0 0 10 10" aria-hidden="true"><path d="M2 1l2 2-1 1.3c.6 1.2 1.5 2.1 2.7 2.7L7 6l2 2-1.3 1.3C4.6 9 1 5.4.7 2.3z" fill="#fff"/></svg>
        03 5618 2947
      </li>
      <li class="contact-item">
        <svg viewBox="0 0 10 10" aria-hidden="true"><rect x="2.5" y="1" width="5" height="3" fill="#fff"/><rect x="1" y="4" width="8" height="5" rx="1" fill="#fff"/></svg>
        03 5619 7084
      </li>
      <li class="contact-item">
        <svg viewBox="0 0 10 10" aria-hidden="true"><rect x="1" y="2" width="8" height="6" fill="#fff"/><path d="M1 2l4 3.4L9 2" stroke="#4a4a4a" stroke-width="1" fill="none"/></svg>
        admin@wrenfieldent.example.com.au
      </li>
      <li class="contact-item">
        <svg viewBox="0 0 10 10" aria-hidden="true"><circle cx="5" cy="5" r="4" fill="#fff"/><path d="M1 5h8M5 1c-2 2.5-2 5.5 0 8M5 1c2 2.5 2 5.5 0 8" stroke="#4a4a4a" stroke-width=".7" fill="none"/></svg>
        wrenfieldent.example.com.au
      </li>
    </ul>
  </section>

  <section class="card card-back" aria-label="Business card back">
    <p class="brand-name">KM Facial Plastics</p>
    <p class="locations">Ashvale • Corrin • Elmbrook • Tarrow • Northgate CBD</p>
  </section>
</body>
</html>
```